Bring my website out of the dark ages!

Website redesign for Velmar Consulting
www.velmarqx.com and www.trundlebox.ca
Currently dark (black), small font, boring, old
Want something simple, bright, fun, modern, clean and professional
Flexible content, any ideas appreciated
In business since 1998, focused on long term client relationships and being there when it matters.
Specialize solutions for clients based on their needs, vision and budget, not what the IT market thinks is the latest and greatest (and most profitable).
Want to eventually add helpful content (videos) and testimonials to the site for the benefit of the visitor

Target Market(s)

Anyone looking for IT services - target is a business with 25-100 employees.

Industry/Entity Type

It Company

Coding

Coded - Design and coding required

Number of Pages Required

4 page

Colors

Designer to choose colors to be used in the design.

Requirements
Must have
• Bright, clean, simple, no scrolling, fast
Nice to have
• Neat animation of some kind
Should not have
• scrolling
• too much information

```html
<!DOCTYPE html>
<html lang="en">
<head>
<meta charset="utf-8">
<title>Velmar Consulting — The Technology Your Business Needs</title>
<link rel="stylesheet" href="https://fonts.googleapis.com/css2?family=Cinzel:wght@400&family=Raleway:ital,wght@0,300;0,400;0,700;1,700&display=swap">
<style>
  :root {
    --page-bg: #ffffff;
    --ink: #2e2e2e;
    --ink-soft: #8a8a8a;
    --ink-nav: #4a4a4a;
    --brand-grey: #9a9a9a;
    --accent: #e3ac3c;
    --card-top: #e6e6e6;
    --card-bottom: #a2a2a2;
    --card-title: #ffffff;
    --header-rule: #e4e4e4;
  }
  * { box-sizing: border-box; margin: 0; padding: 0; }
  html, body {
    width: 1200px; height: 743px; overflow: hidden;
    background: var(--page-bg);
  }
  .page {
    position: relative;
    width: 1200px; height: 743px;
    font-family: "Raleway", sans-serif;
    color: var(--ink);
  }
  .site-header {
    position: absolute; top: 0; left: 0; right: 0; height: 100px;
    border-top: 1px solid var(--header-rule);
  }
  .brand {
    position: absolute; left: 31px; top: 40px;
    font-family: "Raleway", sans-serif;
    font-weight: 300; font-size: 27px; letter-spacing: 0.5px;
    color: var(--brand-grey); text-transform: lowercase;
    white-space: nowrap;
  }
  .main-nav {
    position: absolute; top: 50px; right: 24px;
    display: flex; align-items: center; gap: 28px;
  }
  .main-nav a {
    font-size: 10px; letter-spacing: 2px; text-transform: uppercase;
    color: var(--ink-nav); text-decoration: none;
  }
  .search-icon { width: 12px; height: 12px; margin-left: -18px; }
  .intro { position: absolute; top: 138px; left: 0; right: 0; text-align: center; }
  .intro-title {
    font-family: "Cinzel", serif; font-weight: 400;
    font-size: 28px; letter-spacing: 1px; color: #333;
  }
  .intro-text {
    width: 960px; margin: 24px auto 0;
    font-size: 13.5px; line-height: 23px; font-weight: 400;
    color: var(--ink-soft); letter-spacing: 0.3px;
  }
  .intro-text strong { font-weight: 700; font-style: italic; color: #555; }
  .pillars {
    position: absolute; top: 270px; left: 27px;
    display: flex; gap: 24px;
  }
  .pillar {
    width: 365px; height: 366px;
    background: linear-gradient(180deg, var(--card-top) 0%, var(--card-bottom) 100%);
    padding: 20px 24px 0; text-align: center;
  }
  .pillar-title {
    font-family: "Cinzel", serif; font-weight: 400;
    font-size: 29px; color: var(--card-title); letter-spacing: 1px;
    line-height: 38px;
  }
  .pillar-text {
    margin-top: 10px; font-size: 17.5px; line-height: 28px; color: var(--ink);
  }
  .footer-rule {
    position: absolute; top: 712px; left: 109px; width: 978px;
    height: 1.5px; background: var(--accent);
  }
</style>
</head>
<body>
<div class="page">
  <header class="site-header">
    <div class="brand">Velmar Consulting</div>
    <nav class="main-nav">
      <a href="#">IT Services</a>
      <a href="#">Resources + Links</a>
      <a href="#">Contact</a>
      <svg class="search-icon" viewBox="0 0 12 12" aria-label="Search">
        <circle cx="5" cy="5" r="3.8" fill="none" stroke="var(--accent)" stroke-width="1.3"/>
        <line x1="7.8" y1="7.8" x2="11.2" y2="11.2" stroke="var(--accent)" stroke-width="1.4"/>
      </svg>
    </nav>
  </header>

  <section class="intro">
    <h1 class="intro-title">THE TECHNOLOGY YOUR BUSINESS NEEDS</h1>
    <p class="intro-text">From day one, Velmar has strived to serve its clients with honesty and integrity while providing them with the best technology solutions for their business needs. In doing so, we evoke teamwork and client collaboration to earn the privilege to be <strong>your partner in technology solutions.</strong></p>
  </section>

  <section class="pillars">
    <article class="pillar">
      <h2 class="pillar-title">Experience</h2>
      <p class="pillar-text">Choose an IT consulting company with experience in managing and developing technology solutions. Velmar IT Solutions offers a wide range of professional services in technical innovation that strategically streamline and maximize business performance +&nbsp;potential.</p>
    </article>
    <article class="pillar">
      <h2 class="pillar-title">Goals</h2>
      <p class="pillar-text">Our goal is to ensure that you spend less time on day-to-day operations maximizing company efficiency +&nbsp;expansion possibilities. If you need help with any area of your IT solution, contact us today to have our consultants work with you to develop the right solution.</p>
    </article>
    <article class="pillar">
      <h2 class="pillar-title">Results</h2>
      <p class="pillar-text">We pride ourselves on relationships that produce results. Working together with clients, our long-term alliances bring success to all parties involved. Great companies work with great companies. We share the same values and visions as our clients resulting in successful long term partnerships.</p>
    </article>
  </section>

  <div class="footer-rule"></div>
</div>
</body>
</html>
```